Letterhead for Law Firm - Logo already prepared

I previously used to prepare a logo which I was quite pleased with, a copy is attached for your reference. I would like the font of the logo to be all the same size, rather than the 'S' and 'L' being larger than the other letters.
I have copies of the attached in other formats if necessary.
I need a letterhead prepared which is virtually identical to the draft attached, however I will be adding an address, phone number, fax number, mobile number and email. I will provide these details with whoever can assist me.
I will also be providing insurance details to be listed at the foot of the page.
Finally, I need the file to be supplied as a high resolution pdf with 2mm bleed.
If you require any further information, please do not hesitate to contact me.

```html
<!DOCTYPE html>
<html lang="en">
<head>
<meta charset="utf-8">
<title>Halvorsen Legal – Letterhead</title>
<link rel="stylesheet" href="https://fonts.googleapis.com/css2?family=Cinzel:wght@500&family=Ubuntu:wght@500&display=swap">
<style>
  :root {
    --backdrop: #999999;
    --paper: #ffffff;
    --ink: #141414;
    --brand-orange: #f07226;
    --brand-orange-deep: #b4521a;
    --brand-red: #8e2418;
    --brand-red-light: #b2361f;
    --highlight: #f9a35a;
    --footer-text: #ffffff;
  }
  * { margin: 0; padding: 0; box-sizing: border-box; }
  html, body {
    width: 847px;
    height: 1200px;
    overflow: hidden;
    background: var(--backdrop);
  }
  .letterhead {
    position: absolute;
    left: 42px;
    top: 62px;
    width: 762px;
    height: 1075px;
    background: var(--paper);
    overflow: hidden;
    box-shadow: 0 0 2px rgba(0, 0, 0, 0.35);
  }
  .brand {
    position: absolute;
    left: 44px;
    top: 50px;
    display: flex;
    align-items: center;
    gap: 14px;
  }
  .brand-mark {
    width: 96px;
    height: 96px;
    border-radius: 50%;
    background: var(--brand-orange);
  }
  .brand-name {
    font-family: "Cinzel", "Times New Roman", serif;
    font-weight: 500;
    font-size: 36px;
    letter-spacing: 0.5px;
    color: var(--ink);
    line-height: 1;
  }
  .footer-wave {
    position: absolute;
    left: 0;
    bottom: 0;
    width: 762px;
    height: 1075px;
    pointer-events: none;
  }
  .contact {
    position: absolute;
    right: 44px;
    top: 966px;
    text-align: right;
    font-family: "Ubuntu", "Helvetica", sans-serif;
    font-weight: 500;
    font-size: 12px;
    line-height: 18px;
    color: var(--footer-text);
  }
  .contact-address { margin-bottom: 18px; }
</style>
</head>
<body>
  <main class="letterhead">
    <header class="brand">
      <div class="brand-mark"></div>
      <div class="brand-name">HALVORSEN LEGAL</div>
    </header>

    <svg class="footer-wave" viewBox="0 0 762 1075" aria-hidden="true">
      <defs>
        <linearGradient id="band-orange" x1="0" y1="0" x2="1" y2="0">
          <stop offset="0" stop-color="var(--brand-orange)"/>
          <stop offset="1" stop-color="var(--brand-orange-deep)"/>
        </linearGradient>
        <linearGradient id="band-red" x1="0" y1="0" x2="1" y2="0">
          <stop offset="0" stop-color="var(--brand-red-light)"/>
          <stop offset="1" stop-color="var(--brand-red)"/>
        </linearGradient>
      </defs>
      <path d="M0,1003 Q330,1062 762,856 L762,1075 L0,1075 Z" fill="url(#band-red)"/>
      <path d="M0,1008 Q330,1070 762,898 L762,1075 L0,1075 Z" fill="url(#band-orange)"/>
      <path d="M0,1010 Q330,1072 762,900" fill="none" stroke="var(--highlight)" stroke-width="1.5" opacity="0.8"/>
    </svg>

    <address class="contact">
      <div class="contact-address">address</div>
      <div class="contact-phone">98-5120-3377</div>
      <div class="contact-web">www.halvorsenlegal.com</div>
    </address>
  </main>
</body>
</html>
```